依頼詳細
商品は布マスクになりますが、取り急ぎ添付の不織布マスクの内容で構いせん。
全体のイメージで決定したいと思います。
決定後に布マスクの詳細をお伝えしますので、完成品に仕上げて頂きたいと思います。

製品形状はPP袋(PPのベースは透明もしくはアルミ銀)
袋サイズ:W130xH180mm+ヘッダー部分H20mm

印刷は4色分解でも構いませんが、中国印刷の為、あまり複雑過ぎない程度の色使いでお願いします。

急ぎ提案なのでイメージだけでも早く提案してもらえば助かります。
説明不足で申し訳ございませんが、不明点はご連絡お願い致します。
記載項目
PP袋(PPのベースは透明もしくはアルミ銀)

印刷は4色分解でも構いませんが、中国グラビア印刷(8色まで)の為、あまり複雑過ぎない程度の色使いでお願いします。版代のコストも抑えたいです。
希望イメージ
シンプル 複雑
単色 カラフル
暗い 明るい
日常 高級
遊び心 厳粛
未来的 伝統的
女性的 男性的
希望する色
青系、水色系、無彩色系
納品ファイル
• イラストレーター形式 (.ai)
補足説明

お客様の選定により

たくさんのご提案ありがとうございました
またの機会にも是非またご提案お願い致します。

```html
<!DOCTYPE html>
<html lang="ja">
<head>
<meta charset="utf-8">
<title>不織布マスク パッケージ</title>
<link href="https://fonts.googleapis.com/css2?family=Noto+Sans+JP:wght@500;700;900&display=swap" rel="stylesheet">
<style>
  :root {
    --navy: #1d3564;
    --blue: #2a8fd2;
    --sky: #a9d6ec;
    --sky-deep: #8fc7e3;
    --sky-pale: #c6e5f3;
    --white: #ffffff;
    --header-line: #e6c9d3;
    --hole: #dfe3e8;
  }
  * { margin: 0; padding: 0; box-sizing: border-box; }
  html, body { width: 790px; height: 1200px; overflow: hidden; background: var(--white); }
  body { font-family: "Noto Sans JP", sans-serif; color: var(--navy); }

  .package { position: relative; width: 790px; height: 1200px; overflow: hidden; }

  .header {
    position: absolute; left: 0; top: 0; width: 790px; height: 56px;
    background: var(--white); border: 2px solid var(--header-line); border-bottom: none;
  }
  .hang-hole {
    position: absolute; left: 362px; top: 18px; width: 66px; height: 18px;
    border-radius: 9px; background: var(--hole); border: 2px solid var(--header-line);
  }

  .body-panel {
    position: absolute; left: 0; top: 56px; width: 790px; height: 1144px;
    background: linear-gradient(180deg, var(--sky-pale) 0%, var(--sky) 45%, var(--sky-deep) 100%);
    border: 2px solid var(--header-line); border-top: none;
  }

  .product-photo {
    position: absolute; left: 395px; top: 150px; width: 395px; height: 900px;
    background: radial-gradient(ellipse at 60% 40%, #f1f4f7 0%, #dfe8ef 35%, #c2dcea 70%, rgba(169,214,236,0) 100%);
  }

  .type-banner { position: absolute; left: 37px; top: 92px; display: flex; height: 58px; }
  .type-banner .material {
    width: 350px; background: var(--navy); color: var(--white);
    font-weight: 700; font-size: 40px; line-height: 58px; text-align: center; letter-spacing: 1px;
  }
  .type-banner .usage {
    width: 369px; background: var(--white); color: var(--navy);
    font-weight: 700; font-size: 40px; line-height: 58px; text-align: center; letter-spacing: 1px;
    border: 3px solid var(--navy);
  }

  .headline {
    position: absolute; left: 44px; top: 168px;
    font-weight: 900; font-size: 70px; line-height: 80px; color: var(--navy); letter-spacing: 1px;
  }

  .blocked-item {
    position: absolute; width: 96px; height: 96px; border-radius: 50%;
    background: var(--blue); color: var(--white);
    display: flex; align-items: center; justify-content: center; text-align: center;
    font-weight: 700; font-size: 20px; line-height: 1.2;
  }
  .blocked-item.pollen { left: 57px; top: 329px; font-size: 24px; }
  .blocked-item.dust { left: 181px; top: 329px; }
  .blocked-item.virus { left: 57px; top: 444px; }
  .blocked-item.pm { left: 181px; top: 444px; font-size: 24px; }

  .block-word {
    position: absolute; left: 62px; top: 536px;
    font-weight: 900; font-size: 44px; line-height: 52px; color: var(--navy);
  }

  .mask-drawing {
    position: absolute; left: 40px; top: 630px; width: 290px; height: 200px;
    background: linear-gradient(180deg, #bfe1f1, #b2dbee); border-radius: 12px;
  }

  .claim {
    position: absolute; left: 40px; top: 900px; font-weight: 900; color: var(--navy);
  }
  .claim .rate { color: var(--blue); font-size: 80px; line-height: 80px; }
  .claim .rate small { font-size: 52px; }
  .claim .virus { font-size: 54px; }
  .claim .micron { font-size: 22px; font-weight: 700; }
  .claim .filter { display: block; font-size: 52px; line-height: 66px; margin-top: 4px; }

  .notes {
    position: absolute; left: 40px; top: 1064px; width: 720px;
    font-size: 11px; font-weight: 500; line-height: 17px; color: var(--navy);
  }

  .size-badge {
    position: absolute; left: 614px; top: 880px; width: 168px; height: 168px; border-radius: 50%;
    background: var(--sky); border: 4px solid var(--white);
    display: flex; flex-direction: column; align-items: center; justify-content: center; color: var(--navy);
  }
  .size-badge .label { font-size: 20px; font-weight: 700; color: var(--blue); }
  .size-badge .size { font-size: 44px; font-weight: 900; line-height: 50px; }
  .size-badge .dims { font-size: 13px; font-weight: 700; }
</style>
</head>
<body>
<div class="package">
  <div class="header"><div class="hang-hole"></div></div>
  <div class="body-panel"></div>

  <div class="product-photo" role="img" aria-label="白い不織布マスクを着けた女性の横顔の写真"></div>

  <div class="type-banner">
    <div class="material">不織布マスク</div>
    <div class="usage">使い切りタイプ</div>
  </div>

  <h1 class="headline">高密度<br>フィルターが</h1>

  <div class="blocked-item pollen">花粉</div>
  <div class="blocked-item dust">ハウス<br>ダスト</div>
  <div class="blocked-item virus">ウィルス<br>粉末</div>
  <div class="blocked-item pm">PM2.5</div>

  <div class="block-word">ブロック</div>

  <div class="mask-drawing" role="img" aria-label="プリーツ付き不織布マスクの線画イラスト"></div>

  <p class="claim">
    <span class="rate">99<small>%</small></span><span class="virus">ウィルス飛沫</span><span class="micron">（3μm）</span>
    <span class="filter">カットフィルター使用</span>
  </p>

  <p class="notes">※フィルター性能試験による結果です。<br>※すべての粒子を完全に防ぐものではありません。使用感には個人差があります。</p>

  <div class="size-badge">
    <span class="label">サイズ</span>
    <span class="size">ふつう</span>
    <span class="dims">約17.5cm × 9.5cm</span>
  </div>
</div>
</body>
</html>
```